Menu Design Project for New Catering company

I would like to see my menus in a warm, inviting format. I prepare food for small intimate dinners, business lunches, picnics, parties, weddings and rehearsal dinners. I work with clients to help create their dream whether it includes items on my menu or to prepare very personal dishes that bring them warm memories of a special time or moment.

Target Market(s)

Organizations, wedding and or event planners

Industry/Entity Type

Catering

Requirements
Must have
• I would like to include the logo that is included in the attachment below. I also included a copy of the poster Lio Brenn created for me. I hope this helps. Please be creative. I am a very happy, cheerful person that enjoys cooking and having fun. I would like the design to represent my personality as well as my food. When I cater I treat my customers like an extension of my family and it comes across to them with everything I do for them. I hope this can somehow be reflected in your designs.
Should not have
• I'm open to all ideas and don't want to limit your creativity.

```html
<!DOCTYPE html>
<html lang="en">
<head>
<meta charset="utf-8">
<title>Sage Hill Catering – Buffet Menu</title>
<link href="https://fonts.googleapis.com/css2?family=Source+Sans+3:wght@400;600;700;800&display=swap" rel="stylesheet">
<style>
  :root{
    --green:#3aa845;
    --ink:#1a1a1a;
    --black:#000;
    --white:#fff;
    --photo-warm-1:#7a4a33;
    --photo-warm-2:#c9a27a;
    --photo-pale-1:#f2efec;
    --photo-pale-2:#b9aaa3;
  }
  *{margin:0;padding:0;box-sizing:border-box}
  html,body{width:1200px;height:729px;overflow:hidden;background:var(--black)}
  body{font-family:"Source Sans 3",Arial,sans-serif;color:var(--ink);position:relative}
  .abs{position:absolute}
  sup{font-size:.6em;vertical-align:.55em;line-height:0}
  ul{list-style:none}

  .photo-buffet{left:0;top:0;width:298px;height:146px;
    background:linear-gradient(160deg,var(--photo-warm-1),var(--photo-warm-2) 60%,#e8e2dc)}
  .panel{left:298px;top:0;width:902px;height:713px;background:var(--white)}
  .photo-desserts{left:900px;top:433px;width:300px;height:280px;
    background:linear-gradient(180deg,var(--white),var(--photo-pale-1) 35%,var(--photo-pale-2))}

  .section-title{font-weight:700;color:var(--green);font-size:24.5px;letter-spacing:.4px;line-height:1}
  .page-title{left:321px;top:62px;font-size:42px;font-weight:800;color:var(--green);letter-spacing:.5px;line-height:1}
  .intro{left:321px;top:113px;font-size:11.6px;line-height:13.4px;white-space:nowrap}
  .intro strong{font-size:12.8px}

  .brand-name{left:990px;top:88px;width:100px;text-align:center;font-size:17px;font-weight:700;color:var(--green);line-height:1;white-space:nowrap}

  /* left column */
  .dark{color:var(--white)}
  .appetizers{left:43px;top:191px;width:222px}
  .app-list{margin-top:14px;font-size:10.3px;font-weight:700;line-height:12.9px}
  .app-list li{display:flex;justify-content:space-between;white-space:nowrap}
  .app-list .price{font-weight:400}
  .note{margin-top:10px;font-size:8px;font-style:italic;line-height:10px}
  .salads-title{left:43px;top:371px}
  .salad{position:absolute;left:43px;width:240px}
  .item-name{font-size:13.2px;font-weight:700;line-height:14px;letter-spacing:.2px;white-space:nowrap}
  .item-desc{font-size:10.5px;line-height:12.9px;margin-top:1px;white-space:nowrap}
  .dark .item-desc{line-height:12.6px}

  /* entrees */
  .entrees-title{left:321px;top:191px}
  .entree{position:absolute;width:300px}
  .price{display:block;padding-left:172px;font-size:10.5px;line-height:12.9px}
  .price-inline{position:absolute;left:172px;bottom:0;font-size:10.5px;line-height:12.9px}

  .sides-title{left:607px;top:479px}
  .sides-title{top:428px}
  .sides{left:607px;top:462px;font-size:10.6px;line-height:12.9px;white-space:nowrap}
  .sides li::before{content:"• "}

  .desserts{left:921px;top:191px}
  .desserts ul{margin-top:17px;font-size:10.6px;font-weight:700;line-height:12.9px}
  .drinks{left:921px;top:325px}
  .drinks ul{margin-top:17px;font-size:10.8px;line-height:12.9px;white-space:nowrap}

  .web{left:621px;top:679px;font-size:16px;letter-spacing:1.1px;font-weight:700;color:var(--green);line-height:1}
</style>
</head>
<body>
  <div class="abs photo-buffet" role="img" aria-label="Photo of the caterer standing beside a buffet of chafing dishes"></div>
  <div class="abs panel"></div>
  <div class="abs photo-desserts" role="img" aria-label="Photo of cupcakes and a layered cake on a dessert table"></div>

  <h1 class="abs page-title">BUFFET</h1>
  <p class="abs intro">Priced per person and includes: <strong>1 Entree, 2 Sides or 1 Salad + 1 Side, and 1 Dessert.</strong><br>
  Quotes to add additional entrée(s) and/or sides are available upon request. If you don't see exactly what you are<br>
  looking for we will be happy to work with you to accommodate your requests.&nbsp; Appetizers and drinks are priced<br>
  separately below.</p>

  <div class="abs brand-name">Sage Hill</div>

  <section class="abs appetizers dark">
    <h2 class="section-title">APPETIZERS</h2>
    <ul class="app-list">
      <li><span>Sweet and Spicy Meatballs</span><span class="price-a"><sup>$</sup>3<sup>00</sup>/person</span></li>
      <li><span>Pinwheels (various) -</span></li>
      <li><span>&nbsp; with salsas and/or dips</span><span class="price-a"><sup>$</sup>3<sup>00</sup>/person</span></li>
      <li><span>Stuffed Mushrooms</span><span class="price-a"><sup>$</sup>3<sup>00</sup>/person</span></li>
      <li><span>Mini fried chicken and waffles</span></li>
      <li><span>&nbsp; drizzled with maple syrup</span><span class="price-a"><sup>$</sup>4<sup>00</sup>/person</span></li>
      <li><span>Shrimp cocktails with cocktail sauce</span><span class="price-a"><sup>$</sup>4<sup>00</sup>/person</span></li>
    </ul>
    <p class="note">(Priced per appetizer/per person.<br>Number of servings per appetizer - 6)</p>
  </section>

  <h2 class="abs section-title salads-title dark" style="color:var(--green)">SALADS</h2>
  <div class="salad dark" style="top:412px"><h3 class="item-name">CHOPPED SALAD</h3>
    <p class="item-desc">Lettuce, Cinnamon Candied Pecans, Green Onions,<br>Celery, Blue Cheese Vinaigrette and Blue Cheese<br>Crumbles</p></div>
  <div class="salad dark" style="top:481px"><h3 class="item-name">SPINACH SALAD</h3>
    <p class="item-desc">Fresh Spinach, Red Onions, Candied Pecans and<br>Strawberries (when strawberries are available and/<br>or in season)</p></div>
  <div class="salad dark" style="top:550px"><h3 class="item-name">HOUSE SALAD</h3>
    <p class="item-desc">Mixed Greens, Tomatoes, Carrots, Cucumbers,<br>Croutons and Choice of two types of Dressing<br>(Ranch, Honey Mustard, Italian, or Blue Cheese)</p></div>

  <h2 class="abs section-title entrees-title">ENTREES</h2>

  <div class="entree" style="left:321px;top:232px">
    <h3 class="item-name">LASAGNA SUPREME ROLL-UP</h3>
    <p class="item-desc">Lasagna noodles topped with ricotta, mozzarella and<br>parmesan cheese, beef, sausage and pepperoni in a thick<br>rich meat sauce.</p>
    <span class="price-inline"><sup>$</sup>12<sup>00</sup>/person</span>
  </div>
  <div class="entree" style="left:321px;top:295px">
    <h3 class="item-name">PORK TENDERLOIN WITH<br>MARSALA MUSHROOM SAUCE</h3>
    <p class="item-desc">Tender lightly breaded pork tenderloin medallions topped<br>with delicious sautéed mushrooms all simmered in Marsala<br>wine and heavy cream to develop a rich, decadent sauce.</p>
    <span class="price"><sup>$</sup>12<sup>00</sup>/person</span>
  </div>
  <div class="entree" style="left:321px;top:391px">
    <h3 class="item-name">SMOTHERED CHICKEN</h3>
    <p class="item-desc">Honey mustard grilled chicken breast topped with sautéed<br>mushrooms, crispy bacon, Monterey and cheddar chicken<br>served with a creamy honey mustard sauce.</p>
    <span class="price"><sup>$</sup>12<sup>00</sup>/person</span>
  </div>
  <div class="entree" style="left:321px;top:472px">
    <h3 class="item-name">HOT BROWN</h3>
    <p class="item-desc">Sliced roast turkey seated atop toasted bread and smothered<br>with a rich Mornay sauce—all broiled until golden brown<br>and topped with crisp bacon strips and tomato.</p>
    <span class="price"><sup>$</sup>12<sup>00</sup>/person</span>
  </div>
  <div class="entree" style="left:321px;top:557px">
    <h3 class="item-name">GRANDMA'S BOURBON MAPLE<br>GLAZED HAM</h3>
    <p class="item-desc">Don't worry, you don't have to be 21 to enjoy this tender,<br>juicy glazed ham.</p>
    <span class="price-inline"><sup>$</sup>10<sup>00</sup>/person</span>
  </div>

  <div class="entree" style="left:607px;top:226px">
    <h3 class="item-name">GRILLED OR SMOKED CHICKEN BREASTS</h3>
    <p class="item-desc">Cooked as requested, plain or glazed with a nice, sweet<br>southern BBQ sauce.</p>
    <span class="price-inline"><sup>$</sup>10<sup>00</sup>/person</span>
  </div>
  <div class="entree" style="left:607px;top:286px">
    <h3 class="item-name">PULLED PORK BBQ</h3>
    <p class="item-desc">Tender smoked shredded pork in a sweet, spicy BBQ sauce,<br>buns (onions and dill pickles on the side).</p>
    <span class="price"><sup>$</sup>10<sup>00</sup>/person</span>
  </div>
  <div class="entree" style="left:607px;top:354px">
    <h3 class="item-name">HAWAIIAN MEATBALLS</h3>
    <p class="item-desc">Beef meatballs, pineapple chunks, onions and peppers<br>served in a sweet sauce served along with fluffy white rice<br>side.</p>
    <span class="price-inline"><sup>$</sup>10<sup>00</sup>/person</span>
  </div>

  <h2 class="abs section-title sides-title">SIDES</h2>
  <ul class="abs sides">
    <li>Broccoli Casserole</li>
    <li>Garlic Roasted Broccoli and Carrots</li>
    <li>Honey Glazed Carrots</li>
    <li>Macaroni Salad</li>
    <li>Old Fashioned Green Beans</li>
    <li>Pasta Salad</li>
    <li>Potato Salad</li>
    <li>Potatoes – Garlic Mashed, Scalloped, or Baked</li>
    <li>Southern Baked Beans</li>
    <li>Stewed Tomatoes</li>
    <li>Sweet &amp; Sour Slaw</li>
    <li>Sweet Corn (Creamed, Skillet Fried or Corn on the Cob)</li>
    <li>Sweet Potato Casserole</li>
  </ul>

  <section class="abs desserts">
    <h2 class="section-title">DESSERTS</h2>
    <ul><li>Cheesecakes</li><li>Cream Pies</li><li>Cupcakes</li><li>Fruit Pies</li><li>Key Lime Pie</li></ul>
  </section>
  <section class="abs drinks">
    <h2 class="section-title">DRINKS</h2>
    <ul>
      <li>12 oz. canned Soft Drinks - <sup>$</sup>1<sup>00</sup></li>
      <li>16 oz. bottled water - <sup>$</sup>1<sup>00</sup></li>
      <li>Gallon Tea (sweet or unsweetened) - <sup>$</sup>6<sup>00</sup></li>
    </ul>
  </section>

  <div class="abs web">www.sagehillcatering.com</div>
</body>
</html>
```